Velmora Water Purification

We need a website set up on a "Free account" WordPress platform. (This is the type of Wordpress site that you can sign up for and create online for free (not a server-hosted type.)
The website will be for a water purification company. They install devices in homes to purify the water for safer drinking, bathing, and cleaning.
Our logo is attached. Please keep color scheme of the website consistent with the logo.
Water Purification

```html
<!DOCTYPE html>
<html lang="en">
<head>
<meta charset="utf-8">
<title>Velmora Water Purification</title>
<link href="https://fonts.googleapis.com/css2?family=Cabin:wght@400;500;600;700&display=swap" rel="stylesheet">
<style>
:root{
  --blue:#3d78c2;
  --blue-dark:#2f63a6;
  --ink:#222;
  --muted:#555;
  --grey-bg:#f2f2f2;
  --white:#fff;
  --black:#000;
}
*{box-sizing:border-box;margin:0;padding:0}
html,body{width:1200px;height:1200px;overflow:hidden;background:var(--white)}
body{font-family:'Cabin',sans-serif;color:var(--ink)}
.stage{position:absolute;left:0;top:0;width:1500px;height:1500px;transform:scale(.8);transform-origin:0 0}
.page{position:absolute;left:450px;top:0;width:602px;height:1500px;background:var(--white)}
.abs{position:absolute}
.topbar{left:0;top:0;width:602px;height:25px;background:var(--blue);color:var(--white);font-size:7px}
.topbar .contact{position:absolute;top:9px;display:flex;align-items:center;gap:5px}
.header{left:0;top:25px;width:602px;height:50px}
.brand{position:absolute;left:32px;top:17px;display:flex;align-items:center;gap:6px;color:var(--blue);font-weight:700;font-size:13px}
.brand .dot{width:12px;height:12px;border-radius:50%;background:var(--blue)}
.nav a{position:absolute;top:0;height:50px;line-height:58px;font-size:8px;font-weight:600;color:var(--ink);text-decoration:none}
.nav a.active{background:var(--blue);color:var(--white);width:40px;text-align:center}
.photo{background:linear-gradient(120deg,#4f7d2f,#8fb45a 55%,#d9b98f)}
.hero{left:0;top:75px;width:602px;height:221px}
.hero-line{left:0;top:296px;width:602px;height:2px;background:var(--blue)}
.h2{color:var(--blue);font-size:10px;font-weight:600;letter-spacing:1px;text-transform:uppercase}
.center{text-align:center;width:602px;left:0}
.para{font-size:7px;line-height:12px;color:var(--ink)}
.btn{position:absolute;display:flex;align-items:center;justify-content:center;font-size:7px;font-weight:700;letter-spacing:.5px;text-transform:uppercase}
.btn-blue{background:var(--blue);color:var(--white)}
.feature{left:0;top:443px;width:602px;height:195px}
.feature .wrap{position:absolute;inset:0}
.feature .h3{color:var(--white);font-size:10px;font-weight:600;letter-spacing:.6px}
.arrows{left:525px;top:612px;width:45px;height:18px;display:flex;gap:1px}
.arrows span{flex:1;background:var(--white);border:1px solid #ccc;display:flex;align-items:center;justify-content:center}
.grey{left:0;top:638px;width:602px;height:210px;background:var(--grey-bg)}
.product-img{left:34px;top:679px;width:96px;height:143px;background:linear-gradient(160deg,#e8e3dc,#c9c1b6);box-shadow:1px 1px 3px rgba(0,0,0,.4)}
.product-title{left:144px;top:679px;font-size:10px;font-weight:600;letter-spacing:.6px}
.small{font-size:5.2px;line-height:10.5px;text-align:justify;color:var(--ink)}
.quote{left:380px;top:679px;width:190px;height:120px;background:var(--blue);border:1px solid #6d9bd6;color:var(--white);text-align:center}
.follow{left:0;top:890px;width:602px;display:flex;justify-content:center;gap:5px}
.follow span{width:24px;height:24px;border-radius:50%;background:var(--blue);box-shadow:0 2px 0 #ccc}
.news{left:0;top:964px;width:602px;height:211px}
.news li{list-style:none;position:absolute;left:34px;width:275px;font-size:7px;line-height:11.5px;color:var(--white);padding-left:10px}
.news li::before{content:"»";position:absolute;left:0}
.input{left:200px;top:1271px;width:240px;height:26px;background:var(--blue);color:var(--white);font-size:8px;font-weight:600;display:flex;align-items:center;justify-content:center}
.subscribe{left:281px;top:1304px;width:78px;height:23px;background:var(--black);color:var(--white);font-size:8px;font-weight:700;display:flex;align-items:center;justify-content:center}
.footer{left:0;top:1363px;width:602px;height:137px;background:var(--black);color:var(--white)}
.footer h4{position:absolute;top:12px;font-size:8.5px;font-weight:500}
.footer ul{position:absolute;top:33px;list-style:none;font-size:6.5px;line-height:14px;color:#ddd}
.footer ul li::before{content:"›";margin-right:7px}
.field{position:absolute;left:458px;width:107px;height:15px;border:1px solid #888;font-size:4.5px;color:#aaa;padding:4px 4px}
.legal{position:absolute;top:118px;font-size:4.5px;color:#bbb}
</style>
</head>
<body>
<div class="stage">
<div class="page">

  <div class="abs topbar">
    <div class="contact" style="left:384px">
      <svg width="11" height="8" viewBox="0 0 11 8"><rect x=".5" y=".5" width="10" height="7" fill="none" stroke="#fff"/><path d="M.5 .5l5 4 5-4" fill="none" stroke="#fff"/></svg>
      info@velmora-water.com
    </div>
    <div class="contact" style="left:500px">
      <svg width="8" height="8" viewBox="0 0 8 8"><path d="M1 1c1-1 2 0 2 1s-1 1 0 2 1 1 1 0 1-1 2 0 1 2 0 2C4 7 0 3 1 1z" fill="#fff"/></svg>
      040-555-010-220
    </div>
  </div>

  <div class="abs header">
    <div class="brand"><span class="dot"></span>Velmora</div>
    <nav class="nav">
      <a class="active" style="left:188px">Home</a>
      <a style="left:256px">About Velmora</a>
      <a style="left:362px">Water Purifier</a>
      <a style="left:455px">Services</a>
      <a style="left:524px">Contact Us</a>
    </nav>
  </div>

  <div class="abs hero photo" role="img" aria-label="Child drinking from a clear plastic water bottle outdoors on green grass"></div>
  <div class="abs hero-line"></div>

  <div class="abs h2 center" style="top:322px">About Us</div>
  <p class="abs para center" style="top:345px;padding:0 32px">Lorem Ipsum is simply dummy text of the printing and typesetting industry. Lorem Ipsum has been the industry's standard dummy text ever since the 1500s, when an unknown printer took a galley of type and scrambled it to make a type specimen book. It has survived not only five centuries, but also the leap into electronic typesetting, remaining essentially unchanged.</p>
  <div class="btn btn-blue" style="left:257px;top:395px;width:85px;height:18px">Read More</div>

  <section class="abs feature">
    <div class="wrap photo" style="background:linear-gradient(135deg,#c9d3dc,#8fa6bd 50%,#e6e0da)" role="img" aria-label="Smiling couple beside a home water purifier dispenser filling glasses"></div>
    <svg class="wrap" width="602" height="195" viewBox="0 0 602 195"><polygon points="290,0 602,0 602,195 240,195" fill="#3d78c2"/></svg>
    <div class="abs h3" style="left:296px;top:14px">HOME WATER PURIFIERS</div>
    <p class="abs" style="left:294px;top:36px;width:274px;font-size:7.3px;line-height:12px;color:#fff;text-align:justify">There are many variations of passages of Lorem Ipsum available, but the majority have suffered alteration in some form, by injected humour, or randomised words which don't look even slightly believable. If you are going to use a passage of Lorem Ipsum, you need to be sure there isn't anything embarrassing hidden in the middle of text. All the Lorem Ipsum generators on the Internet tend to repeat predefined chunks as necessary, making this the first true generator on the Internet.</p>
    <div class="btn" style="left:294px;top:140px;width:78px;height:22px;background:#fff;color:var(--blue)">Read More</div>
  </section>
  <div class="abs arrows">
    <span><svg width="6" height="8"><path d="M5 1L1 4l4 3" fill="none" stroke="#222"/></svg></span>
    <span><svg width="6" height="8"><path d="M1 1l4 3-4 3" fill="none" stroke="#222"/></svg></span>
  </div>

  <section class="abs grey"></section>
  <div class="abs h2" style="left:34px;top:654px">Our Products</div>
  <div class="abs product-img" role="img" aria-label="Woman standing next to a countertop water filter unit"></div>
  <div class="abs product-title">SED UT PERSPICIATIS UNDE OMNIS</div>
  <p class="abs small" style="left:144px;top:698px;width:218px">At vero eos et accusamus et iusto odio dignissimos ducimus qui blanditiis praesentium voluptatum deleniti atque corrupti quos dolores et quas molestias excepturi sint occaecati cupiditate non provident, similique sunt in culpa qui officia deserunt mollitia animi, id est laborum et dolorum fuga. Et harum quidem rerum facilis est et expedita distinctio. Nam libero tempore, cum soluta nobis est eligendi optio cumque nihil impedit quo minus id quod maxime placeat facere possimus, omnis voluptas assumenda est.</p>
  <div class="btn btn-blue" style="left:307px;top:785px;width:54px;height:15px;font-size:6px">View More</div>

  <div class="abs h2" style="left:380px;top:654px">Our Client Says</div>
  <div class="abs quote">
    <svg class="abs" style="left:55px;top:14px" width="80" height="48" viewBox="0 0 80 48">
      <text x="2" y="20" fill="#fff" font-size="14" font-family="Cabin,sans-serif" font-weight="700">"</text>
      <text x="68" y="20" fill="#fff" font-size="14" font-family="Cabin,sans-serif" font-weight="700">"</text>
      <circle cx="40" cy="24" r="23" fill="#1b2a3c" stroke="#fff" stroke-width="1.5"/>
      <circle cx="40" cy="18" r="7" fill="#fff"/>
      <path d="M27 38c1-8 7-11 13-11s12 3 13 11z" fill="#fff"/>
    </svg>
    <p class="abs" style="left:20px;top:70px;width:150px;font-size:5.5px;line-height:8.5px;font-weight:600">At vero eos et accusamus et iusto odio dignissimos ducimus qui blanditiis praesentium voluptatum deleniti atque corrupti quos dolores .</p>
    <p class="abs" style="right:22px;top:105px;font-size:5.5px;font-weight:600">- de Finibus Bonorum</p>
  </div>

  <div class="abs h2 center" style="top:861px">Follow Us</div>
  <div class="abs follow" aria-label="Social links">
    <span></span><span></span><span></span><span></span><span></span>
  </div>

  <section class="abs news">
    <div class="abs photo" style="inset:0;background:linear-gradient(135deg,#2c4e7a,#6a85a8 50%,#d7dde3)" role="img" aria-label="Video still of a technician with purification equipment"></div>
    <svg class="abs" style="left:0;top:0" width="602" height="211" viewBox="0 0 602 211"><polygon points="0,0 295,0 377,211 0,211" fill="#3d78c2"/>
      <circle cx="468" cy="106" r="14" fill="none" stroke="#fff" stroke-width="1.5"/><polygon points="464,99 464,113 475,106" fill="#fff"/></svg>
    <div class="abs" style="left:36px;top:12px;color:#fff;font-size:10px;font-weight:600;letter-spacing:.6px">LATEST NEWS</div>
    <ul>
      <li style="top:38px">Nemo enim ipsam voluptatem quia voluptas sit aspernatur aut odit aut fugit</li>
      <li style="top:74px">At vero eos et accusamus et iusto odio dignissimos ducimus qui blanditiis praesentium voluptatum deleniti atque corrupti quos.</li>
      <li style="top:110px">Neque porro quisquam est, qui dolorem ipsum quia dolor sit amet, consectetur, adipisci velit</li>
      <li style="top:147px">Quis autem vel eum iure reprehenderit qui in ea voluptate velit esse quam nihil molestiae consequatur, vel illum qui dolorem eum fugiat quo voluptas nulla pariatur.</li>
    </ul>
  </section>

  <div class="abs h2 center" style="top:1199px">Subscribe to our Newsletter</div>
  <p class="abs center" style="top:1229px;padding:0 70px;font-size:6px;line-height:12px;font-weight:600">Neque porro quisquam est, qui dolorem ipsum quia dolor sit amet, consectetur, adipisci velit, sed quia non numquam eius modi tempora incidunt ut labore et dolore magnam aliquam quaerat voluptatem.</p>
  <div class="abs input">Enter Your Email Address</div>
  <div class="abs subscribe">Subscribe</div>

  <footer class="abs footer">
    <h4 style="left:33px">Velmora</h4>
    <p class="abs" style="left:33px;top:31px;width:130px;font-size:6px;line-height:11px;color:#ddd">At vero eos et accusamus et iusto odio dignissimos ducimus qui blanditiis praesentium voluptatum caecati.</p>
    <h4 style="left:193px">Services</h4>
    <ul style="left:193px"><li>sequi nesciunt</li><li>dolore magnam</li><li>quaerat voluptatem</li><li>quis nostrum</li></ul>
    <h4 style="left:320px">Products</h4>
    <ul style="left:322px"><li>accusantium doloremque</li><li>nostrum exercitationem</li><li>ullam corporis</li><li>molestiae consequatur</li></ul>
    <h4 style="left:458px">Contact Us</h4>
    <div class="field" style="top:33px">ENTER YOUR NAME</div>
    <div class="field" style="top:54px">EMAIL ADDRESS</div>
    <div class="abs" style="left:458px;top:76px;width:42px;height:15px;background:var(--blue);border:1px solid #aaa;font-size:6.5px;display:flex;align-items:center;justify-content:center">Submit</div>
    <div class="abs" style="left:33px;top:106px;width:532px;height:1px;background:#333"></div>
    <span class="legal" style="left:33px">Copy Rights Reserved @ 2017 Velmora</span>
    <span class="legal" style="left:462px">Terms &amp; Conditions</span>
    <span class="legal" style="left:530px">Privacy Policy</span>
  </footer>

</div>
</div>
</body>
</html>
```